IT services company requires Letterhead design

We need a professional letterhead designed to be used for general correspondence with customers, quotes, invoices etc. We are a new IT services company specialising in computer servicing and repairs and mobile and tablet repairs. Attached are templates that my printing company have supplied, my logos, an interpretation of our website for you to get a feel of the company. Details to be included on the letterhead are

Company Number – 4738261
VAT Number - 518337942
Registered Address – 14-16 Brambly Lane, London, E4 9QT

Phone – 01632 487215
Email – sales@quorvent.com
Web – www.quorvent.com

I would prefer for the top of the letterhead to just have the company logo on a white background and the rest of the details on the bottom of the letterhead but I am open to design ideas.

Thanks

```html
<!DOCTYPE html>
<html lang="en">
<head>
<meta charset="utf-8">
<title>Quorvent Letterhead</title>
<link href="https://fonts.googleapis.com/css2?family=Ubuntu:ital,wght@1,500;1,700&display=swap" rel="stylesheet">
<style>
  :root {
    --purple: #8e2a94;
    --purple-deep: #7a2482;
    --navy: #26266b;
    --lavender: #f0e9f4;
    --white: #ffffff;
    --teal: #1b6f8c;
    --plum: #6b3c8c;
    --rose: #de4a6a;
    --red: #e5433a;
  }
  * { box-sizing: border-box; margin: 0; padding: 0; }
  html, body { width: 848px; height: 1200px; overflow: hidden; background: var(--white); }
  body { font-family: "Ubuntu", sans-serif; font-style: italic; font-weight: 700; color: var(--navy); }
  .letterhead { position: relative; width: 848px; height: 1200px; overflow: hidden; background: var(--white); }

  .band { position: absolute; left: 0; width: 848px;
    background: linear-gradient(90deg, var(--teal) 0%, var(--plum) 35%, var(--rose) 70%, var(--red) 100%); }
  .band--top { top: 0; height: 32px; }
  .band--bottom { bottom: 0; height: 34px; }

  .brand-block { position: absolute; left: 0; top: 0; width: 274px; height: 103px;
    background: linear-gradient(90deg, var(--purple-deep), var(--purple)); }
  .brand-block__name { position: absolute; left: 52px; top: 44px; font-size: 36px; font-weight: 700;
    color: var(--white); letter-spacing: 0.5px; }
  .brand-name { position: absolute; left: 58px; top: 114px; font-size: 38px; font-weight: 700; color: var(--purple); }
  .brand-rule { position: absolute; left: 43px; top: 170px; width: 185px; height: 2px; background: var(--purple); }

  .company-details { position: absolute; left: 591px; top: 52px; height: 88px; border-left: 2px solid #b7b7c4;
    padding-left: 18px; font-size: 11.5px; font-weight: 700; line-height: 1; }
  .company-details__row { display: flex; align-items: center; height: 24px; }
  .company-details__label { width: 114px; }
  .company-details__row--vat .company-details__label { width: 103px; }
  .company-details__value { border: 1.5px solid var(--navy); padding: 3px 6px; }
  .company-details__address { line-height: 24px; }

  .feature-area { position: absolute; left: 239px; top: 429px; width: 372px; height: 276px;
    border-radius: 14px; background: var(--lavender); }

  .footer-rule { position: absolute; left: 182px; top: 1065px; width: 483px; height: 2px; background: var(--purple); }
  .contact { position: absolute; top: 1088px; width: 160px; text-align: center; font-size: 11.5px; font-weight: 700; }
  .contact svg { display: block; margin: 0 auto 8px; height: 30px; }
  .contact--phone { left: 185px; }
  .contact--email { left: 342px; }
  .contact--web { left: 500px; }
</style>
</head>
<body>
<main class="letterhead">
  <div class="band band--top" role="img" aria-label="Multicoloured geometric triangle band"></div>

  <div class="brand-block"><span class="brand-block__name">Quorvent</span></div>
  <div class="brand-name">Quorvent</div>
  <div class="brand-rule"></div>

  <section class="company-details">
    <div class="company-details__row"><span class="company-details__label">Company Number</span><span class="company-details__value">4738261</span></div>
    <div class="company-details__row company-details__row--vat"><span class="company-details__label">VAT Number</span><span class="company-details__value">518337942</span></div>
    <div class="company-details__address">Address: 14-16 Brambly Lane,<br>London, E4 9QT</div>
  </section>

  <div class="feature-area" role="img" aria-label="Faint pale lavender laptop illustration as a background motif"></div>

  <div class="footer-rule"></div>

  <div class="contact contact--phone">
    <svg viewBox="0 0 18 30" width="18" aria-hidden="true">
      <rect x="1" y="1" width="16" height="28" rx="3" fill="var(--purple)"/>
      <rect x="3" y="5" width="12" height="18" fill="var(--white)"/>
      <circle cx="9" cy="26" r="1.5" fill="var(--white)"/>
    </svg>
    01632 487215
  </div>
  <div class="contact contact--email">
    <svg viewBox="0 0 30 30" width="30" aria-hidden="true">
      <rect x="2" y="7" width="26" height="17" fill="var(--purple)"/>
      <path d="M2 7 L15 17 L28 7" fill="none" stroke="var(--white)" stroke-width="1.5"/>
    </svg>
    sales@quorvent.com
  </div>
  <div class="contact contact--web">
    <svg viewBox="0 0 30 30" width="30" aria-hidden="true">
      <text x="15" y="24" text-anchor="middle" font-family="Ubuntu, sans-serif" font-weight="700" font-size="26" fill="var(--purple)">@</text>
    </svg>
    www.quorvent.com
  </div>

  <div class="band band--bottom" role="img" aria-label="Multicoloured geometric triangle band"></div>
</main>
</body>
</html>
```